Hotel Company Personal Business Card

This is a hotel business, personal business card. Need it sleek, professional, and sharp looking. I have a design attached that we can work with. My turnaround time is April 8th. I would need the cards by then. One side only color, the other side all details. This is flexible depending on the designs you come up with. I would like a boutique, unique, modern type of touch to the business card. Memorable type of card that people will want to keep.

Target Market(s)

Business professionals

Industry/Entity Type

Hospitality/Hotels & Resorts

Contact Information for Business Card

Name, email, phone number, address, and company name. Anything unique

Font styles to use
Serif
Sans Serif

Colors

Designer to choose colors to be used in the design.

Requirements
Nice to have
• Neutral colors. Eye popping logo. Sleek design. Boutique feel. Hint of color.

```html
<!DOCTYPE html>
<html lang="en">
<head>
<meta charset="utf-8">
<title>Harbor Crest Hotel Group – Business Card</title>
<link rel="stylesheet" href="https://fonts.googleapis.com/css2?family=Lato:wght@400;700&display=swap">
<style>
  :root {
    --canvas-bg: #e6e6e6;
    --card-dark: #25262b;
    --card-dark-soft: #2c2d32;
    --logo-stone: #8e8b87;
    --accent-tan: #8b7763;
    --text-light: #ffffff;
    --faint-mark: #393a3f;
  }
  * { margin: 0; padding: 0; box-sizing: border-box; }
  html, body { width: 1200px; height: 1021px; overflow: hidden; }
  body {
    background: var(--canvas-bg);
    font-family: "Lato", sans-serif;
    position: relative;
  }
  .card {
    position: absolute;
    width: 434px;
    height: 759px;
    background: var(--card-dark);
    box-shadow: 0 2px 8px rgba(0,0,0,0.22);
    overflow: hidden;
  }
  .card--front { left: 109px; top: 98px; }
  .card--back  { left: 582px; top: 106px; }

  .logo-backdrop { position: absolute; left: 0; width: 100%; background: var(--logo-stone); }
  .logo-band { position: absolute; left: 0; width: 100%; background: var(--card-dark); }
  .accent-rule { position: absolute; left: 0; width: 100%; height: 9px; background: var(--accent-tan); }

  .brand-name {
    position: absolute; left: 0; width: 100%;
    text-align: center;
    font-family: "Lato", sans-serif;
    font-weight: 700;
    color: var(--text-light);
    text-transform: uppercase;
    white-space: nowrap;
  }
  .brand-name__main { font-size: 38px; letter-spacing: 4px; line-height: 44px; }
  .brand-name__sub  { font-size: 21px; letter-spacing: 7px; line-height: 26px; }
  .brand-name--faint { color: var(--faint-mark); }

  .line {
    position: absolute; left: 0; width: 100%;
    text-align: center; color: var(--text-light);
    font-size: 20px; line-height: 28px; white-space: nowrap;
  }
  .holder-name { color: var(--accent-tan); font-size: 28px; font-weight: 700; line-height: 34px; letter-spacing: -0.5px; }
  .holder-title { font-size: 20px; }
  .contact { font-size: 20px; letter-spacing: 0.2px; }
  .address { font-size: 19.5px; letter-spacing: 0.3px; }

  .rule { position: absolute; height: 1.5px; background: var(--accent-tan); }
  .icon-row { position: absolute; left: 182px; top: 465px; width: 70px; height: 20px; }
</style>
</head>
<body>

  <section class="card card--front" aria-label="Business card, details side">
    <div class="logo-backdrop" style="top:0;height:181px;"></div>
    <div class="logo-band" style="top:181px;height:103px;"></div>
    <div class="accent-rule" style="top:284px;"></div>

    <div class="brand-name brand-name__main" style="top:196px;">Harbor Crest</div>
    <div class="brand-name brand-name__sub" style="top:243px;">Hotel Group</div>

    <div class="line holder-name" style="top:374px;">Daniel Mercer</div>
    <div class="line holder-title" style="top:413px;">Managing Director</div>

    <div class="rule" style="left:70px;top:474px;width:109px;"></div>
    <svg class="icon-row" viewBox="0 0 70 20" aria-hidden="true">
      <g fill="var(--accent-tan)">
        <circle cx="10" cy="10" r="9.5"/>
        <circle cx="35" cy="10" r="9.5"/>
        <circle cx="60" cy="10" r="9.5"/>
      </g>
      <path d="M7 5.5 l2 -0.5 1.2 3 -1.3 1 q1 2 2.8 2.8 l1 -1.3 3 1.2 -0.5 2 q-6 0.5 -8.2 -8.2z" fill="#fff"/>
      <rect x="29.5" y="6" width="11" height="8" rx="1" fill="#fff"/>
      <path d="M29.8 6.5 L35 10.5 L40.2 6.5" fill="none" stroke="var(--accent-tan)" stroke-width="1.1"/>
      <circle cx="60" cy="10" r="5.5" fill="none" stroke="#fff" stroke-width="1.3"/>
      <path d="M54.5 10 H65.5 M60 4.5 Q56.5 10 60 15.5 M60 4.5 Q63.5 10 60 15.5" fill="none" stroke="#fff" stroke-width="1"/>
    </svg>
    <div class="rule" style="left:254px;top:474px;width:109px;"></div>

    <div class="line contact" style="top:502px;">021-555 018 342</div>
    <div class="line contact" style="top:532px;">hello@harborcrest.com</div>
    <div class="line contact" style="top:561px;">www.harborcrest.com</div>

    <div class="rule" style="left:109px;top:608px;width:216px;"></div>

    <div class="line address" style="top:629px;">14 LINDEN PARK RD.</div>
    <div class="line address" style="top:654px;">MAYFORD, N 4417</div>
  </section>

  <section class="card card--back" aria-label="Business card, brand side">
    <div class="brand-name brand-name__main brand-name--faint" style="top:196px;">Harbor Crest</div>
    <div class="brand-name brand-name__sub brand-name--faint" style="top:243px;">Hotel Group</div>

    <div class="logo-backdrop" style="top:474px;height:179px;"></div>
    <div class="logo-band" style="top:653px;height:106px;"></div>

    <div class="brand-name brand-name__main" style="top:669px;">Harbor Crest</div>
    <div class="brand-name brand-name__sub" style="top:717px;">Hotel Group</div>
  </section>

</body>
</html>
```